Company Brochure promoting our Managed Services Business (MSP)

Objective: Is the brochure meant to generate leads, educate potential clients, and promote our Managed Services Business.
Target Audience: is for Small to medium size business.
A managed service provider like Brillora Advisory Group handles a variety of different responsibilities for Business
. We oversee vital IT resources such as:
Email
Cloud integration
Data storage
Networking
Cybersecurity
File backup
Help desk services
Our firm also provides remote monitoring services and updates. As part of our managed service provider solutions, we will continually report on the performance and quality of your network. We can even help your organization acquire new hardware and software.
At Brillora Advisory Group we specialize in empowering commercial businesses with robust IT solutions tailored to enhance efficiency, security, and scalability. With years of expertise in Managed Services, we understand the unique challenges businesses face in today’s digital landscape.
Call-to-Action (CTA):
Encourage readers to contact you, visit your website, or schedule a consultation.
you can get an overview of BAG at www..brillorabag.example.
Layout: Opt for a clean, easy-to-read layout with well-defined sections.
Imagery:
Include professional photos, custom graphics, or icons that represent your services.
Avoid generic stock images when possible.
Format: Tri-fold, bi-fold, depending on the amount of information.
We would like to have a section of the "e5" from our web site.
I have attached the Logos.
Target Market(s)
Small to Medium Business
Look and feel

```html
<!DOCTYPE html>
<html lang="en">
<head>
<meta charset="utf-8">
<title>Brillora Advisory Group – Managed Services Brochure</title>
<link href="https://fonts.googleapis.com/css2?family=Barlow:wght@600;700;800&family=Poppins:wght@400;500;600&display=swap" rel="stylesheet">
<style>
:root{
  --teal:#164f5e;
  --teal-dark:#0f3d49;
  --ink:#1d2a30;
  --muted:#3b474c;
  --paper:#ffffff;
  --shade:#efefef;
  --bg-top:#2b2b2b;
  --bg-bottom:#9a9a9a;
}
*{margin:0;padding:0;box-sizing:border-box}
html,body{width:995px;height:1200px;overflow:hidden}
body{background:linear-gradient(160deg,var(--bg-top),var(--bg-bottom));font-family:"Poppins",sans-serif;color:var(--ink);position:relative}
.page{position:absolute;width:400px;height:517px;background:var(--paper);overflow:hidden}
.page--about{left:84px;top:78px}
.page--cover{left:524px;top:78px}
.page--services{left:84px;top:629px}
.page--results{left:524px;top:632px}
.abs{position:absolute}
.heading{font-family:"Barlow",sans-serif;font-weight:700;text-transform:uppercase;letter-spacing:.2px}
.body-text{font-size:5.3px;line-height:7.8px;text-align:justify}

/* brand mark */
.brand{display:flex;align-items:center;gap:5px}
.brand__square{background:var(--teal);flex:none}
.brand__name{font-family:"Poppins",sans-serif;font-weight:500;color:var(--teal);text-transform:uppercase;line-height:1.05}

/* About page */
.about__panel{left:58px;top:105px;width:342px;height:280px;background:var(--teal);clip-path:polygon(22px 0,100% 0,100% 100%,0 100%,0 22px)}
.about__divider{left:110px;top:105px;width:1px;height:280px;background:rgba(255,255,255,.55)}
.about__label{left:60px;top:300px;width:170px;transform:rotate(-90deg);transform-origin:left top;color:#fff;font-size:17px;letter-spacing:1.5px;white-space:nowrap}
.about__copy{left:126px;top:148px;width:242px;color:#fff}
.about__copy h2{font-size:10px;margin-bottom:4px}
.about__copy p{margin-bottom:10px}
.contact__title{left:58px;top:408px;font-family:"Poppins",sans-serif;font-weight:600;font-size:10px;color:var(--teal)}
.contact__item{display:flex;gap:4px;font-size:6.6px;line-height:8.6px;color:var(--ink)}
.contact__item svg{flex:none;margin-top:1px}

/* Cover */
.cover__shade{left:0;top:0;width:400px;height:517px}
.cover__band{left:0;top:105px;width:45px;height:280px;background:var(--teal)}
.cover__image{left:45px;top:105px;width:280px;height:280px;background:radial-gradient(circle at 45% 45%,#f0b7a0 0,#6e8fc2 12%,#1d4f80 35%,#0e2a4f 70%,#0a1d38 100%)}
.cover__rule{left:200px;top:105px;width:1px;height:115px;background:rgba(255,255,255,.8)}
.cover__title{left:213px;top:128px;color:#fff;font-size:16px;line-height:19.6px;font-weight:800}
.cover__url-rule{left:232px;top:462px;width:105px;height:1px;background:var(--teal)}
.cover__url{left:232px;top:471px;font-size:9px;color:var(--ink)}

/* Services */
.services__hero{left:0;top:0;width:400px;height:174px;background:linear-gradient(180deg,#3b3f49 0%,#5b6068 60%,#767a80 100%)}
.services__title{left:43px;top:37px;color:#fff;font-size:15px}
.services__rule{left:43px;top:63px;width:314px;height:1px;background:rgba(255,255,255,.7)}
.services__sub{left:43px;top:83px;color:#fff;font-size:10px}
.services__intro{left:43px;top:101px;width:314px;color:#fff}
.service__icon{left:43px;width:55px;height:55px;background:var(--teal);clip-path:polygon(0 0,100% 0,100% 80%,80% 100%,0 100%)}
.service__text{left:115px;width:242px}
.service__text h3{font-size:9.6px;color:var(--teal);margin-bottom:3px}
.service__text p{color:var(--muted)}
.stripe{left:0;bottom:0;width:400px;height:6px;background:var(--teal)}

/* Results */
.results__hero{left:0;top:0;width:400px;height:205px;background:linear-gradient(135deg,#5d6670 0%,#3a4a55 45%,#6f5a48 80%,#8b6e55 100%)}
.results__band{left:0;top:205px;width:400px;height:202px;background:var(--teal)}
.results__title{left:40px;top:227px;color:#fff;font-size:15px}
.results__title sup{font-size:8px}
.results__copy{left:157px;top:264px;width:210px;color:#fff}
.results__copy h3{font-size:12px;margin:6px 0 4px}
.results__badge{left:39px;top:274px}
.results__mission{left:40px;top:426px;font-size:12px;color:var(--teal)}
.results__mission-text{left:40px;top:446px;width:327px;color:var(--muted)}
</style>
</head>
<body>

<!-- About -->
<section class="page page--about">
  <svg class="abs" style="left:0;top:0" width="400" height="517" aria-hidden="true">
    <path d="M193 0 V100 Q193 112 184 121 L162 143" fill="none" stroke="var(--teal)" stroke-width=".8"/>
    <path d="M0 247 H42 Q50 247 56 241 L58 238" fill="none" stroke="var(--teal)" stroke-width=".8"/>
  </svg>
  <div class="abs about__panel"></div>
  <div class="abs about__divider"></div>
  <div class="abs heading about__label">About Us</div>
  <div class="abs about__copy">
    <h2 class="heading">Our Vision</h2>
    <p class="body-text">Brillora Advisory Group empowers your business to thrive in the digital age. Our team of expert consultants specializes in transforming your technology landscape – streamlining operations, enhancing security, and driving innovation. Whether you're looking to implement cutting-edge solutions or optimize existing systems, we tailor our approach to meet your unique needs, ensuring you stay ahead of the competition and achieve your strategic goals</p>
    <h2 class="heading">Who We Are</h2>
    <p class="body-text">Brillora Advisory Group empowers businesses of all sizes to thrive in the digital age by leveraging our extensive experience, deep industry knowledge, and advanced technological solutions. We are committed to delivering superior results and fostering long-term partnerships with our clients, helping them achieve their goals and stay ahead of the competition.</p>
    <h2 class="heading">How We Can Help</h2>
    <p class="body-text">With over 150 years of experience, we bring unparalleled expertise and insights to every project, ensuring superior outcomes for our clients. Using innovation strategies, we stay at the forefront of technological advancements, continually innovating and adapting our solutions to meet the evolving needs of our clients and the industry. Understanding that every business is unique, we tailor our solutions to fit the specific requirements and objectives of each client, ensuring maximum impact and value.</p>
  </div>

  <div class="abs contact__title">Contact Info</div>
  <div class="abs contact__item" style="left:58px;top:437px">
    <svg width="7" height="8" viewBox="0 0 7 8"><path d="M3.5 7.5C1.5 5 1 4 1 3a2.5 2.5 0 0 1 5 0c0 1-.5 2-2.5 4.5z" fill="none" stroke="var(--teal)" stroke-width=".6"/><circle cx="3.5" cy="3" r=".9" fill="none" stroke="var(--teal)" stroke-width=".6"/></svg>
    <span>210 Harbor Lane<br>Suite 40<br>Maple Cove, FL 30000</span>
  </div>
  <div class="abs contact__item" style="left:167px;top:440px">
    <svg width="8" height="8" viewBox="0 0 8 8"><path d="M2 1l1.3 1.8-.8.9c.5 1 1.1 1.6 2 2l.9-.8L7 6.2 6.3 7.2C3.5 7 1 4.5.8 1.8z" fill="none" stroke="var(--teal)" stroke-width=".6"/></svg>
    <span>1-800-555-0147</span>
  </div>
  <div class="abs contact__item" style="left:167px;top:454px">
    <svg width="8" height="8" viewBox="0 0 8 8"><rect x=".5" y="1.5" width="7" height="5" fill="none" stroke="var(--teal)" stroke-width=".6"/><path d="M.5 1.5L4 4.5 7.5 1.5" fill="none" stroke="var(--teal)" stroke-width=".6"/></svg>
    <span>sales@brillorabag.example</span>
  </div>
  <div class="abs contact__item" style="left:58px;top:478px">
    <svg width="8" height="8" viewBox="0 0 8 8"><circle cx="4" cy="4" r="3.3" fill="none" stroke="var(--teal)" stroke-width=".6"/><ellipse cx="4" cy="4" rx="1.4" ry="3.3" fill="none" stroke="var(--teal)" stroke-width=".5"/><path d="M.7 4h6.6" stroke="var(--teal)" stroke-width=".5"/></svg>
    <span>www.brillorabag.example</span>
  </div>
  <div class="abs brand" style="left:298px;top:440px">
    <span class="brand__square" style="width:20px;height:20px"></span>
    <span class="brand__name" style="font-size:6.3px">Brillora<br>Advisory<br>Group</span>
  </div>
</section>

<!-- Cover -->
<section class="page page--cover">
  <svg class="abs cover__shade" viewBox="0 0 400 517" aria-hidden="true">
    <polygon points="337,105 400,160 400,517 150,517 60,400 337,400" fill="var(--shade)"/>
    <path d="M330 105 V390 H58" fill="none" stroke="var(--teal)" stroke-width="1.2"/>
    <path d="M336 105 V396 H58" fill="none" stroke="var(--teal)" stroke-width="1.2"/>
  </svg>
  <div class="abs brand" style="left:200px;top:38px">
    <span class="brand__square" style="width:37px;height:37px"></span>
    <span class="brand__name" style="font-size:12px;line-height:13px">Brillora<br>Advisory<br>Group</span>
  </div>
  <div class="abs cover__band"></div>
  <div class="abs cover__image" role="img" aria-label="Photo of a hand touching a glowing digital technology interface"></div>
  <div class="abs cover__rule"></div>
  <h1 class="abs heading cover__title">Providing<br>Innovative<br>Technology<br>Solutions</h1>
  <div class="abs cover__url-rule"></div>
  <div class="abs cover__url">www.brillorabag.example</div>
</section>

<!-- Services -->
<section class="page page--services">
  <div class="abs services__hero" role="img" aria-label="Darkened photo of hands typing on a laptop with faint technology graphics"></div>
  <h2 class="abs heading services__title">Our Services</h2>
  <div class="abs services__rule"></div>
  <h3 class="abs heading services__sub">Managed Services</h3>
  <p class="abs body-text services__intro">An MSP (Managed Service Provider) is a company that provides IT services and support to businesses. They manage and monitor things like networks, security, software, and technical support, ensuring everything runs smoothly. Businesses pay an MSP regularly (often through a subscription) to take care of their IT needs, instead of having an in-house IT team. This helps businesses focus on their core work while leaving the technical side to experts.</p>

  <div class="abs service__icon" style="top:197px"></div>
  <div class="abs service__text" style="top:199px">
    <h3 class="heading">Account Management Services</h3>
    <p class="body-text">Brillora Advisory Group reduces the burden of administrative tasks so you can focus on what truly matters – growing your business! Let us handle the negotiation and management of your other business services accounts. Our dedicated Account Management Team excels in every aspect of account management, from meticulously crafting RFPs and bids to ensuring seamless contract, lease, and service agreement renewals.</p>
  </div>

  <div class="abs service__icon" style="top:276px"></div>
  <div class="abs service__text" style="top:278px">
    <h3 class="heading">Business Technologies</h3>
    <p class="body-text">Getting ahead in an extremely competitive landscape requires more than just hard work – it demands working smarter. Brillora provides a comprehensive approach, integrating new and existing tools, providing enhanced efficiency, improved communication, security reinforcement, and futureproofing. Let us become your technology partner to embrace the power of innovation and propel your business success with the latest advancements in technology and strategic deployment!</p>
  </div>

  <div class="abs service__icon" style="top:362px"></div>
  <div class="abs service__text" style="top:364px">
    <h3 class="heading">Training &amp; Education Services</h3>
    <p class="body-text">Whether you're looking to boost your sales figures, enhance customer satisfaction, or hone management skills, we've got you covered. Driven by decades of management experience, we carefully craft our expert-led programs to address the specific needs of your professionals at every stage of their career journey.</p>
  </div>

  <div class="abs service__icon" style="top:432px"></div>
  <div class="abs service__text" style="top:434px">
    <h3 class="heading">Workflow Management</h3>
    <p class="body-text">Streamline your processes, boost efficiency, and elevate productivity with our cutting-edge workflow management solutions. From meticulous documentation to real-time monitoring and continuous improvement, we empower you to master every step of your tasks seamlessly. Transform complexity into clarity and drive unparalleled results with our intuitive workflow management tools.</p>
  </div>
  <div class="abs stripe"></div>
</section>

<!-- Results -->
<section class="page page--results">
  <div class="abs results__hero" role="img" aria-label="Photo of a team meeting around a desk with documents and glowing technology icons"></div>
  <div class="abs results__band"></div>
  <h2 class="abs heading results__title">E<sup>5</sup> Exponential Results</h2>
  <svg class="abs results__badge" width="86" height="86" viewBox="0 0 86 86" role="img" aria-label="Five-step methodology badge">
    <circle cx="43" cy="43" r="43" fill="#fff"/>
    <circle cx="43" cy="43" r="33" fill="none" stroke="var(--teal)" stroke-width="1"/>
    <circle cx="43" cy="43" r="26" fill="var(--teal-dark)"/>
  </svg>
  <div class="abs results__copy">
    <p class="body-text">Brillora Advisory Group believes every successful technology initiative requires a structured, results-driven approach. Our 5 E's methodology Evaluate, Enhance, Engineer, Execute, and Evolve is designed to ensure each project not only meets your immediate needs but also positions your organization for long-term success.</p>
    <h3 class="heading">Our Process</h3>
    <p class="body-text">We begin by thoroughly evaluating your current systems and processes to identify opportunities and challenges. From there, we enhance your framework with tailored recommendations, engineer innovative solutions that align with your goals, and execute them with precision. Finally, we partner with you to continuously evolve your technology, ensuring it remains agile and effective in an ever-changing landscape. With the 5 E's, we provide a clear pathway to transformative results.</p>
  </div>
  <h2 class="abs heading results__mission">Our Mission</h2>
  <p class="abs body-text results__mission-text">Brillora Advisory Group empowers your business to thrive in the digital age. Our team of expert consultants specializes in transforming your technology landscape – streamlining operations, enhancing security, and driving innovation. Whether you're looking to implement cutting-edge solutions or optimize existing systems, we tailor our approach to meet your unique needs, ensuring you stay ahead of the competition and achieve your strategic goals</p>
  <div class="abs stripe"></div>
</section>

</body>
</html>
```